Web Design Project - Do It Yourself Website/Blog company

Task Description:
We need a new website for Brellwick.com, an established company that has been around for 10+ years.
Our website is fine, but we believe more is possible.
We are seeking a new look and feel, as well as a new "sales message". We're not sure that visitors to our site immediately understand what we do, and how we are positioned.
We are looking for a new design (including the major text on the pages), for the principal webpages. The physical implementation we can handle.
Our product is do-it-yourself websites and blogs, for home users and small business.
Our system is widget based, with powerful tools and widgets that provide features well beyond "just a website." For instance, we provide all of the mailing list management, security, hosting, and powerful widgets like shopping, discussion forums, payment buttons, etc. Our mission is to put the powerful tools, normally available only on websites costing tens of thousands of dollars, and make them available to people who know nothing about web design, and don't want to learn.
The price for our product begins at “Free” for a website or blog with good functionality but limited storage. For $3 a month, we provide a more robust product including a personalized URL/Domain, more storage and additional tools and for $10 a month customers get a very robust system including outbound email and newsletter capabilities and powerful search engine optimization tools.
The overall goal of the website is to solicit people to sign-up for a free website. Doing so requires no credit card or other obligation, though the customer does need to provide some limited contact information and agree to our EULA.
Our current website is at www.brellwick.com, but we encourage prospective designers to disregard any information they find there directly associated with the product capabilities. We are open and eager to move forward in a new and fresh design direction.
Must have features:
The goal is signup for a free website, so a clear path into the sign-up process is paramount.
Ultimately our goal is to get users who will benefit from our services enough to pay at least $3 a month for services, so a product that targets people with specific needs that they are willing to pay for (businesses/enthusiasts) over casual users (children/teen) is needed.
Target Market: Our core users are small-to-medium sized businesses – usually sole proprietors who are very hands on. We also have a large base of affluent enthusiasts who engage in boating, breeding (dogs/horses), and casual activities. We also have some amateur sports teams, personal family websites and general consumer traffic.
Scope of project: We're looking for the key pages on the site, the wording for the key points on each of the principal pages, and the overall look/feel. We want something that communicates clearly what we do, and why customers should try our product.
Delivery: We're ok with any type of delivery of the finished product. The site can be mocked up in powerpoint, photoshop, or HTML - whatever. We're looking for a site we would want to buy from, that communicates succinctly and clearly what we do, and why we are the best (or, at a minimum takes away the fear of giving us a try). Once we have this, we are open to contracting you to do the physical html implementation, but see this as a seperate project.
Updates
Reason: I haven't seen any designs yet that seemed different enough from what I have to excite me.
To motivate designers, and simplify the project, let's take this approach:
- I only need the homepage (Originally, I was asking for a few pages)
- I'm happy with submission in any format
- Your design doesn't need to have all of the copy. You can greek the small print. I just want to see the overall look, and sales messsage (images, headlines, and section headers). Give me enough that I can easily envision the finished product
Important: As soon as I see any design that interests me, I'll make the money non-refundable
Dale M Brellwick.com
I've just made the money non-refundable, so someone is going to get a payday.
This is the feedback I gave on the most recent design:
"...On the right track. I like this. Best so far.
My only comments:
- A subset of our product is free, so I don't like to say "Try it now", because most users are in fact paying nothing, and yet getting tremendous value.
- We should reference that it is "websites and blogs" .. not just websites.
- If you find a place to put it, we could/should(?) mention three things that might lend credibility to us: 1) In business since 1999, 2) Built over 100,000 websites, 3) My background (Founder/CEO Quillfen Digital, leading consumer software company)
Thank you!
Dale Morrow
PS I am making the money non-refundable. You are in the lead....
Target Market(s)
Small business (under 10 employees)
Homeowners Associations
Owner's groups
Clubs
Music groups
People with expensive assets they want a website for (boats, second homes)
Industry/Entity Type
Credit Card
Requirements
Must have
- Compelling visual impact
Sales message that communicates why we are the best option (ease of use?, low cost? Power?)
Copy examples (Section headings, and enough text for each section that we can tell what the sales message is)
Should not have
- We want something that makes us look amazing!

```html
<!DOCTYPE html>
<html lang="en">
<head>
<meta charset="utf-8">
<title>Brellwick – Web &amp; Email Marketing Services</title>
<link href="https://fonts.googleapis.com/css2?family=Roboto+Condensed:wght@400;700&family=Roboto+Slab:wght@400&family=Arimo:wght@400;700&display=swap" rel="stylesheet">
<style>
:root{
  --blue:#0a6fbf;
  --blue-dark:#0d4f8a;
  --blue-deep:#0b5394;
  --ink:#333;
  --muted:#666;
  --line:#d8d8dc;
  --panel:#e8e8ec;
  --band:#f1f1f3;
  --white:#fff;
  --footer:#c9c9ce;
}
*{box-sizing:border-box;margin:0;padding:0}
html,body{width:912px;height:1200px;overflow:hidden;background:var(--white);font-family:"Arimo",Arial,sans-serif;color:var(--ink)}
.page{position:relative;width:912px;height:1200px}
.abs{position:absolute}

/* header */
.site-header{left:0;top:0;width:912px;height:72px;background:linear-gradient(#f4f4f6,#e6e6ea)}
.brand{left:41px;top:12px;display:flex;align-items:center;gap:8px}
.brand-mark{width:42px;height:42px;background:var(--blue);border-radius:4px}
.brand-name{font-family:"Roboto Condensed",sans-serif;font-size:34px;color:#777;line-height:30px;letter-spacing:1px}
.brand-tag{font-family:"Roboto Condensed",sans-serif;font-size:10.5px;color:#777;letter-spacing:.5px}
.main-nav{left:463px;top:23px;display:flex;gap:6px}
.main-nav a{font-family:"Roboto Condensed",sans-serif;font-size:14px;text-decoration:none;color:#555;background:var(--white);padding:5px 9px;height:27px;display:block;border-radius:2px}
.main-nav a.active{background:var(--blue);color:var(--white)}
.login{left:813px;top:21px;width:57px;height:31px;background:var(--blue);color:var(--white);font-family:"Roboto Condensed",sans-serif;font-weight:700;font-size:15px;text-align:center;line-height:31px;border-radius:3px;text-decoration:none}

/* hero */
.hero{left:0;top:72px;width:912px;height:251px;background:linear-gradient(#fdfdfd,#e9e9ec)}
.perks{left:46px;top:97px;list-style:none;font-family:"Roboto Slab",serif;font-size:12.5px;color:#555}
.perks li{height:21.6px;display:flex;align-items:center;gap:8px}
.perks svg{width:11px;height:11px}
.cta{left:43px;top:215px;width:166px;height:38px;border-radius:19px;background:linear-gradient(#1a85d6,#0a5aa3);color:var(--white);font-family:"Roboto Condensed",sans-serif;font-weight:700;font-size:20px;display:flex;align-items:center;padding-left:18px;gap:12px;text-decoration:none}
.cta svg{width:24px;height:24px}
.cta-note{left:222px;top:225px;font-family:"Roboto Condensed",sans-serif;font-weight:700;font-size:16px;color:#555}
.pricing{left:150px;top:271px;width:176px;height:30px;background:linear-gradient(#bdbdbd,#9a9a9a);color:var(--white);font-family:"Roboto Slab",serif;font-size:15px;text-align:center;line-height:30px;border-radius:3px;text-decoration:none}
.hero-shot{left:461px;top:85px;width:385px;height:226px;border-radius:3px;background:radial-gradient(circle at 60% 55%,#b9bcc0 0%,#8d9196 35%,#4a3420 70%,#2e1f12 100%)}

/* feature band */
.features{left:0;top:323px;width:912px;height:174px;background:var(--band)}
.feature{width:285px;height:87px;display:flex;gap:9px;padding:10px 0 0 0}
.feature h3{font-family:"Roboto Slab",serif;font-weight:400;font-size:12.5px;color:var(--blue-deep);line-height:14px;margin-top:8px}
.feature p{font-size:9.5px;font-weight:700;color:#888;line-height:11px;margin-top:2px}
.seal{flex:none;width:66px;height:66px}
.divider-v{width:1px;background:var(--line)}
.divider-h{height:1px;background:var(--line)}

/* tiles */
.tile{width:268px;height:108px;background:var(--blue);color:var(--white)}
.tile-icon{position:absolute;left:11px;top:12px;width:59px;height:58px;background:#3c8fd1}
.tile-icon::after{content:"";position:absolute;left:22px;bottom:-8px;border:8px solid transparent;border-bottom:0;border-top-color:#3c8fd1}
.tile-icon svg{width:59px;height:58px}
.tile h4{position:absolute;left:80px;top:12px;font-family:"Roboto Slab",serif;font-weight:400;font-size:12.5px}
.tile p{position:absolute;left:80px;top:31px;width:180px;font-size:9.5px;font-weight:700;line-height:10.5px}
.tile-foot{position:absolute;left:0;bottom:0;width:100%;height:23px;background:var(--blue-deep);font-size:9.5px;font-weight:700;text-align:right;padding:6px 8px 0 0}

/* product & help */
.section-title{font-family:"Roboto Slab",serif;font-size:19px;color:var(--blue);font-weight:400}
.tag-box{left:41px;top:775px;width:572px;height:190px;background:var(--panel);border-radius:3px;padding:13px 0 0 13px;display:flex;flex-wrap:wrap;align-content:flex-start;gap:9px 9px}
.tag{font-size:10px;color:#777;background:var(--white);border-radius:10px;padding:0 10px;height:20px;line-height:20px}
.help-box{left:630px;top:775px;width:241px;height:190px;background:#d4d4da;border-radius:3px}
.help-links{position:absolute;left:12px;top:10px;list-style:none;font-size:10px;font-weight:700;color:#444}
.help-links li{height:18px}
.help-links li::before{content:"▸ ";font-size:8px}
.help-sep{position:absolute;left:0;top:87px;width:100%;height:1px;background:#bdbdc4}
.contact{position:absolute;left:12px;top:98px;font-size:10px;color:#333;line-height:18px}
.contact a{color:var(--blue);text-decoration:none}
.social{position:absolute;display:flex;align-items:center;gap:6px;font-size:12px;font-weight:700;color:var(--blue-deep)}
.social i{display:block;width:12px;height:12px;background:var(--blue-deep)}

/* partners */
.partners{left:49px;top:1005px;width:813px;height:127px;background:var(--white);box-shadow:0 0 4px rgba(0,0,0,.25);border-radius:2px}
.partner{position:absolute;font-size:20px;font-weight:700;color:var(--blue-deep)}
.badge{position:absolute;background:#b7bcc4;border-radius:4px}

/* footer */
.site-footer{left:0;top:1164px;width:912px;height:36px;background:var(--footer);font-size:9.5px;color:var(--white);font-weight:700}
.site-footer nav{position:absolute;left:41px;top:13px}
.site-footer small{position:absolute;right:41px;top:13px;font-size:9.5px;color:#555;font-weight:400}
</style>
</head>
<body>
<div class="page">

<header class="site-header abs">
  <div class="brand abs" style="left:41px">
    <span class="brand-mark"></span>
    <div><div class="brand-name">BRELLWICK</div><div class="brand-tag">WEB &amp; EMAIL MARKETING SERVICES</div></div>
  </div>
  <nav class="main-nav abs">
    <a class="active" href="#">About Brellwick</a><a href="#">Our Product</a><a href="#">Services</a><a href="#">Testimonials</a>
  </nav>
  <a class="login abs" href="#">Log In</a>
</header>

<section class="hero abs"></section>
<ul class="perks abs">
  <li><svg viewBox="0 0 12 12"><path d="M1 6l3 3 7-7" stroke="#2a8ad4" stroke-width="2.4" fill="none"/></svg>Easy drag &amp; drop interface.</li>
  <li><svg viewBox="0 0 12 12"><path d="M1 6l3 3 7-7" stroke="#2a8ad4" stroke-width="2.4" fill="none"/></svg>No programming skills needed.</li>
  <li><svg viewBox="0 0 12 12"><path d="M1 6l3 3 7-7" stroke="#2a8ad4" stroke-width="2.4" fill="none"/></svg>Includes your world class hosting &amp; web address.</li>
  <li><svg viewBox="0 0 12 12"><path d="M1 6l3 3 7-7" stroke="#2a8ad4" stroke-width="2.4" fill="none"/></svg>Affordable pricing for Consumers &amp; Business.</li>
  <li><svg viewBox="0 0 12 12"><path d="M1 6l3 3 7-7" stroke="#2a8ad4" stroke-width="2.4" fill="none"/></svg>Powerful design tools including Image &amp; Text Editors.</li>
</ul>
<a class="cta abs" href="#">GET STARTED <svg viewBox="0 0 24 24"><circle cx="12" cy="12" r="11" fill="#fff"/><path d="M9 6l7 6-7 6z" fill="#0a5aa3"/></svg></a>
<div class="cta-note abs">TRY IT FREE TODAY</div>
<a class="pricing abs" href="#">See Pricing Options</a>
<div class="hero-shot abs" role="img" aria-label="Sample customer website built with Brellwick, featuring a classical marble sculpture photo on a dark ornate theme"></div>

<section class="features abs">
  <div class="abs divider-v" style="left:312px;top:0;height:174px"></div>
  <div class="abs divider-v" style="left:597px;top:0;height:174px"></div>
  <div class="abs divider-h" style="left:41px;top:86px;width:831px"></div>

  <div class="feature abs" style="left:41px;top:0">
    <svg class="seal" viewBox="0 0 66 66"><circle cx="33" cy="33" r="32" fill="#0a6fbf" stroke="#fff" stroke-width="2" stroke-dasharray="4 3"/><circle cx="33" cy="33" r="22" fill="none" stroke="#fff" stroke-width="1.5"/><rect x="25" y="22" width="16" height="21" fill="none" stroke="#fff" stroke-width="2"/><path d="M29 38l9-11" stroke="#fff" stroke-width="2.5"/></svg>
    <div><h3>Get a FREE Website or Blog Today</h3><p>Powerful Design Tools Including Image and Text Editors.</p></div>
  </div>
  <div class="feature abs" style="left:325px;top:0">
    <svg class="seal" viewBox="0 0 66 66"><circle cx="33" cy="33" r="32" fill="#0a6fbf" stroke="#fff" stroke-width="2" stroke-dasharray="4 3"/><circle cx="33" cy="33" r="22" fill="none" stroke="#fff" stroke-width="1.5"/><rect x="22" y="26" width="22" height="15" fill="#fff"/><path d="M22 26l11 9 11-9" stroke="#0a6fbf" stroke-width="1.5" fill="none"/></svg>
    <div><h3>Complete Business Solutions</h3><p>Ecommerce, Email Marketing &amp; SEO just $99 a year.</p></div>
  </div>
  <div class="feature abs" style="left:610px;top:0">
    <svg class="seal" viewBox="0 0 66 66"><circle cx="33" cy="33" r="32" fill="#0a6fbf" stroke="#fff" stroke-width="2" stroke-dasharray="4 3"/><circle cx="33" cy="33" r="22" fill="none" stroke="#fff" stroke-width="1.5"/><ellipse cx="30" cy="30" rx="9" ry="6" fill="#fff"/><ellipse cx="38" cy="37" rx="8" ry="5.5" fill="#fff" stroke="#0a6fbf"/></svg>
    <div><h3>Easy Website Builder and Hosting Company</h3><p>Create your Website or Blog in Minutes</p></div>
  </div>
  <div class="feature abs" style="left:41px;top:87px">
    <svg class="seal" viewBox="0 0 66 66"><circle cx="33" cy="33" r="32" fill="#0a6fbf" stroke="#fff" stroke-width="2" stroke-dasharray="4 3"/><circle cx="33" cy="33" r="22" fill="none" stroke="#fff" stroke-width="1.5"/><path d="M33 20v26M20 33h26M33 20l-4 4M33 20l4 4M33 46l-4-4M33 46l4-4M20 33l4-4M20 33l4 4M46 33l-4-4M46 33l-4 4" stroke="#fff" stroke-width="2" fill="none"/></svg>
    <div><h3>Create a Professional Website</h3><p>Brellwick Website Builder. Drag and Drop. No Skills Required.</p></div>
  </div>
  <div class="feature abs" style="left:325px;top:87px">
    <svg class="seal" viewBox="0 0 66 66"><circle cx="33" cy="33" r="32" fill="#0a6fbf" stroke="#fff" stroke-width="2" stroke-dasharray="4 3"/><circle cx="33" cy="33" r="22" fill="none" stroke="#fff" stroke-width="1.5"/><path d="M21 25h4l3 11h13l2-8H27" stroke="#fff" stroke-width="2.5" fill="none"/><circle cx="30" cy="41" r="2" fill="#fff"/><circle cx="39" cy="41" r="2" fill="#fff"/></svg>
    <div><h3>Business Websites with Brellwick Pro</h3><p>Custom Domain, SEO, Email Marketing &amp; Ecommerce Tools.</p></div>
  </div>
  <div class="feature abs" style="left:610px;top:87px">
    <svg class="seal" viewBox="0 0 66 66"><circle cx="33" cy="33" r="32" fill="#0a6fbf" stroke="#fff" stroke-width="2" stroke-dasharray="4 3"/><circle cx="33" cy="33" r="22" fill="none" stroke="#fff" stroke-width="1.5"/><path d="M26 33l13-7M26 33l13 7" stroke="#fff" stroke-width="2"/><circle cx="26" cy="33" r="4" fill="#fff"/><circle cx="39" cy="26" r="4" fill="#fff"/><circle cx="39" cy="40" r="4" fill="#fff"/></svg>
    <div><h3>Custom Domain and Social Media Sharing</h3><p>Get Found and Drive Traffic with Brellwick Plus $3 a Month.</p></div>
  </div>
</section>

<article class="tile abs" style="left:41px;top:510px">
  <div class="tile-icon"><svg viewBox="0 0 59 58"><rect x="15" y="18" width="29" height="21" fill="#fff"/><path d="M15 18l14.5 12L44 18" stroke="#3c8fd1" stroke-width="2" fill="none"/></svg></div>
  <h4>Grow your Business:</h4><p>Email Marketing Suite, send newsletters, announcements and track every email.</p>
  <div class="tile-foot">Read more ›</div>
</article>
<article class="tile abs" style="left:322px;top:510px">
  <div class="tile-icon"><svg viewBox="0 0 59 58"><path d="M14 14v30h32" stroke="#fff" stroke-width="3" fill="none"/><path d="M17 39l9-12 7 6 11-14" stroke="#fff" stroke-width="3.5" fill="none"/></svg></div>
  <h4>Get Found Today.</h4><p>Build your brand and drive traffic with Search Engine Tools.</p>
  <div class="tile-foot">Read more ›</div>
</article>
<article class="tile abs" style="left:602px;top:510px">
  <div class="tile-icon"><svg viewBox="0 0 59 58"><text x="29.5" y="44" text-anchor="middle" font-family="Arimo,Arial,sans-serif" font-weight="700" font-size="40" fill="#fff">?</text></svg></div>
  <h4>Need Help?</h4><p>Visit our Online Help Center. Quick Reference Guides, FAQ, Webinars and more!</p>
  <div class="tile-foot">Read more ›</div>
</article>
<article class="tile abs" style="left:41px;top:631px">
  <div class="tile-icon"><svg viewBox="0 0 59 58"><path d="M10 17h7l5 18h20l4-13H20" stroke="#fff" stroke-width="3.5" fill="none"/><rect x="20" y="22" width="24" height="12" fill="#fff"/><circle cx="24" cy="42" r="3.5" fill="#fff"/><circle cx="40" cy="42" r="3.5" fill="#fff"/></svg></div>
  <h4>Shopping Made Easy.</h4><p>Simple to use ecommerce tools and buttons to collect money.</p>
  <div class="tile-foot">Read more ›</div>
</article>
<article class="tile abs" style="left:322px;top:631px">
  <div class="tile-icon"><svg viewBox="0 0 59 58"><circle cx="29.5" cy="29" r="16" fill="none" stroke="#fff" stroke-width="2" stroke-dasharray="5 3"/><circle cx="29.5" cy="29" r="8" fill="#fff" opacity=".7"/></svg></div>
  <h4>Explore</h4><p>Build your brand and drive traffic with Search Engine Tools.</p>
  <div class="tile-foot">Read more ›</div>
</article>
<article class="tile abs" style="left:602px;top:631px">
  <div class="tile-icon"><svg viewBox="0 0 59 58"><rect x="20" y="11" width="19" height="36" rx="3" fill="#fff"/><rect x="22.5" y="16" width="14" height="24" fill="#3c8fd1"/></svg></div>
  <h4>Stay Connected.</h4><p>Download Brellwick Connect our Mobile App.</p>
  <div class="tile-foot">Read more ›</div>
</article>

<h2 class="section-title abs" style="left:41px;top:748px">Product &amp; Features</h2>
<div class="tag-box abs">
  <span class="tag">Custom Menus</span><span class="tag">Text Editing Tools</span><span class="tag">Image Editing Tools</span><span class="tag">Photo Galleries</span><span class="tag">Blogging Tools</span>
  <span class="tag">Social Media Sharing</span><span class="tag">Music</span><span class="tag">Video</span><span class="tag">Documents</span><span class="tag">Map Finder</span><span class="tag">Weather Desk</span>
  <span class="tag">Forum</span><span class="tag">Scheduling</span><span class="tag">Calendar</span><span class="tag">RSS</span><span class="tag">Comments</span><span class="tag">Sign In</span><span class="tag">Payment</span>
  <span class="tag">Shopping Tools</span><span class="tag">Polls, Surveys and Forms</span><span class="tag">Real Estate Listing</span><span class="tag">Mortgage Calculator</span>
  <span class="tag">JavaScript</span><span class="tag">Contact Lists</span><span class="tag">Contact Details</span><span class="tag">Search</span><span class="tag">Sign Up/Register</span>
  <span class="tag">Custom Domain Names</span><span class="tag">Search Engine Tools</span><span class="tag">Email Marketing Suite</span><span class="tag">Ecommerce Tools</span>
</div>

<h2 class="section-title abs" style="left:630px;top:748px">Help &amp; Support</h2>
<aside class="help-box abs">
  <ul class="help-links"><li>Webinars</li><li>User Group Forum</li><li>Quick Start Guide</li><li>FAQ</li></ul>
  <div class="social" style="left:150px;top:40px"><i></i>Chirper</div>
  <div class="help-sep"></div>
  <div class="contact">Live Chat: <a href="#">Submit Support Ticket</a><br><a href="#">Email Support</a><br>1-800-555-0142</div>
  <div class="social" style="left:112px;top:152px"><i></i>Friendloop</div>
</aside>

<h2 class="section-title abs" style="left:49px;top:975px">Our Partners</h2>
<div class="partners abs">
  <span class="partner" style="left:45px;top:25px">Searchly</span>
  <span class="partner" style="left:166px;top:25px">Friendloop</span>
  <span class="badge" style="left:289px;top:18px;width:98px;height:42px"></span>
  <span class="partner" style="left:405px;top:25px">Cloudvance</span>
  <span class="partner" style="left:545px;top:25px">Yodelfind</span>
  <span class="badge" style="left:664px;top:22px;width:84px;height:84px"></span>
  <span class="partner" style="left:150px;top:78px">Findra</span>
  <span class="partner" style="left:243px;top:78px">Uplora</span>
  <span class="badge" style="left:366px;top:80px;width:104px;height:24px"></span>
  <span class="partner" style="left:490px;top:78px">Chirper</span>
</div>

<footer class="site-footer abs">
  <nav>Affiliate Program &nbsp;|&nbsp; Privacy Policy &nbsp;|&nbsp; Contact Us &nbsp;|&nbsp; Log In &nbsp;|&nbsp; Terms of Service</nav>
  <small>© 2012 Brellwick.com: The Free Website Builder.</small>
</footer>

</div>
</body>
</html>
```